Grand Bridal Pastry Selling Method needs finishing touches to website.

We have a temporary website located at http://www.brivantaworks.example/qk/.
We are doing a responsive design and have created the architecture (layout). However, we need a professional makeover for the graphic elements and colors of the website. The website will be selling a sales course to mostly women who sell wedding cakes.
The photos within the posted website are for illustrative purposes. We will use our own photos after the website is redone.
We are open to changing the font styles, borders, header, and anything else as long as the layout is not changed.
Target Market(s)
75% women age 25-50 and men 30-60.
Industry/Entity Type
Architecture
Colors
Designer to choose colors to be used in the design.
Look and feel
Each slider illustrates characteristics of the customer's brand and the style your logo design should communicate.

```html
<!DOCTYPE html>
<html lang="en">
<head>
<meta charset="utf-8">
<title>Grand Bridal Pastry Selling Method</title>
<link href="https://fonts.googleapis.com/css2?family=Lato:wght@400;700;900&family=Tinos:ital,wght@0,400;0,700;1,700&display=swap" rel="stylesheet">
<style>
:root{
  --bg:#eeeceb;
  --page:#ffffff;
  --pink:#f2bfcc;
  --pink-light:#f8dde4;
  --pink-dark:#e7a5b6;
  --dark:#333333;
  --text:#3b3b3b;
  --olive:#4f4a2c;
  --grey:#888888;
  --footer:#7b7b7b;
  --footer-dark:#3d3d3d;
  --line:#dcdcdc;
}
*{box-sizing:border-box;margin:0;padding:0}
html,body{width:1041px;height:1200px;overflow:hidden}
body{background:var(--bg);font-family:"Lato",sans-serif;color:var(--text);position:relative}
.page{position:absolute;left:114px;top:31px;width:813px;height:1169px;background:var(--page);border-top:2px solid var(--pink)}
.abs{position:absolute}
.headline{left:132px;top:48px;font-family:"Tinos",serif;font-size:24px;line-height:32px;color:#222}
.headline em{font-style:italic;font-weight:700}
.headline b{font-weight:700}
.call-box{left:729px;top:55px;width:182px;height:52px;border:1px solid #e6e6e6;border-radius:3px;background:linear-gradient(#fff,#f1f1f1);display:flex;align-items:center;padding-left:10px;gap:8px}
.call-box .lbl{font-family:"Tinos",serif;font-size:14px;color:#333;line-height:15px}
.call-box .num{font-family:"Lato",sans-serif;font-size:18px;color:#222;line-height:20px}
.nav{left:130px;top:131px;width:781px;height:57px;display:flex;background:var(--dark)}
.nav a{font-family:"Tinos",serif;font-size:18px;color:#fff;text-decoration:none;display:flex;align-items:center;justify-content:center;border-right:2px solid #222;white-space:nowrap}
.nav a.active{background:var(--pink);color:#333}
.video{left:130px;top:204px;width:504px;height:289px;background:#111}
.video .shot{position:absolute;left:39px;top:24px;width:426px;height:239px;background:linear-gradient(135deg,#6d6656,#3a3a35 60%,#5a3a34)}
.video .title{position:absolute;left:10px;top:7px;font-size:10px;color:#eee;letter-spacing:.3px}
.video .play{position:absolute;left:218px;top:121px;width:68px;height:46px;background:rgba(20,20,20,.85);border-radius:10px}
.video .bar{position:absolute;left:0;bottom:0;width:100%;height:28px;background:linear-gradient(#2a2a2a,#111)}
.video .track{position:absolute;left:0;bottom:27px;width:100%;height:5px;background:#555}
.video .time{position:absolute;left:73px;bottom:8px;font-size:9px;color:#ddd}
.video .brand{position:absolute;right:30px;bottom:8px;font-size:9px;color:#bbb}
.optin{left:667px;top:204px;width:244px;height:289px;background:var(--pink)}
.optin .top{height:146px;background:linear-gradient(var(--pink),var(--pink-light));padding-top:14px;text-align:center;font-size:19px;line-height:28.5px;color:#4a4a38}
.optin .top b{font-weight:700;font-size:22px}
.field{position:absolute;left:14px;width:216px;height:29px;background:#fff;border:1px solid #ead2d8;border-radius:2px;font-size:11px;font-style:italic;color:#999;display:flex;align-items:center;padding-left:28px}
.field svg{position:absolute;left:8px;top:8px}
.optin .nospam{position:absolute;left:19px;top:255px;font-size:9.5px;color:#333}
.btn{position:absolute;background:linear-gradient(#f7cfd9,var(--pink-dark));color:#3a3a3a;font-weight:700;border-radius:2px;display:flex;align-items:center;justify-content:center}
.optin .btn{left:115px;top:243px;width:114px;height:28px;font-size:12px}
.rule{left:150px;width:741px;height:1px;background:linear-gradient(90deg,transparent,#d8d8d8 20%,#d8d8d8 80%,transparent)}
.section-title{left:130px;top:553px;width:781px;text-align:center;font-family:"Tinos",serif;font-weight:700;font-size:20.5px;color:var(--olive)}
.card{position:absolute;top:597px;width:183px;height:322px;border:1px solid #f0d0d8;border-radius:3px;background:#fff;box-shadow:0 3px 3px -1px rgba(0,0,0,.12)}
.card .img{position:absolute;left:11px;top:12px;width:160px;height:102px}
.card h3{position:absolute;left:10px;top:123px;width:162px;font-size:12px;font-weight:700;line-height:17px;color:#3c3c3c}
.card p{position:absolute;left:10px;top:218px;width:162px;font-size:10.5px;line-height:17px;color:#333}
.card .btn{left:50%;margin-left:-40px;bottom:0;width:80px;height:26px;font-size:9.5px;border-radius:3px 3px 0 0}
.card .seen{position:absolute;top:125px;width:100%;text-align:center;font-size:12px;color:#7a6a3a;font-weight:700}
.badge{position:absolute;left:11px;width:160px;height:57px;border:1px solid #f0c9d4;background:#fff;display:flex;align-items:center;justify-content:center}
.badge span{display:block;width:70px;height:22px;background:#d4d4d4;border-radius:3px}
.logo-tile{position:absolute;top:981px;height:58px;border:1px solid #d8d8d8;background:#fff;display:flex;align-items:center;justify-content:center}
.logo-tile span{display:block;background:#c9c9c9;border-radius:3px}
.arrow{position:absolute;top:1000px}
.footer{left:114px;top:1071px;width:813px;height:97px;background:linear-gradient(var(--footer),#8a8a8a)}
.footer .links{position:absolute;left:25px;top:28px;font-size:11px;font-weight:700;color:#fff;white-space:nowrap}
.footer .links i{font-style:normal;margin:0 7px}
.footer .contact{position:absolute;left:25px;top:57px;font-size:11px;color:#fff;display:flex;gap:13px;align-items:center;white-space:nowrap}
.footer .contact span{display:flex;align-items:center;gap:6px}
.footer .split{position:absolute;left:519px;top:22px;width:1px;height:60px;background:#5e5e5e}
.footer .news{position:absolute;left:555px;top:26px;font-size:12.5px;font-weight:700;color:#fff;letter-spacing:.3px}
.footer .news-in{position:absolute;left:554px;top:52px;width:156px;height:24px;background:#fff;font-size:10.5px;font-style:italic;color:#999;padding:5px 10px}
.footer .news-btn{position:absolute;left:710px;top:52px;width:78px;height:24px;background:var(--pink);color:#222;font-weight:700;font-size:13px;display:flex;align-items:center;justify-content:center}
.bottom{left:114px;top:1168px;width:813px;height:32px;background:var(--footer-dark);color:#fff;font-size:11.5px;padding:9px 26px}
.social{position:absolute;right:20px;top:6px;display:flex;gap:6px}
.social span{width:20px;height:20px;border-radius:50%;background:#d8d8d8}
.social span:first-child{background:var(--pink)}
</style>
</head>
<body>
<div class="page"></div>

<div class="abs headline">Cracking the <em>“Secret Code”</em><br>That Unlocks Your <b>Wedding Cake Sales!</b></div>

<div class="abs call-box">
  <svg width="38" height="38" viewBox="0 0 38 38"><circle cx="19" cy="19" r="17" fill="none" stroke="#f2bfcc" stroke-width="3"/><path d="M12 11c2-2 4 0 5 2s0 3-1 4c1 2 3 4 5 5 1-1 2-2 4-1s4 3 2 5c-3 3-8 1-12-3s-6-9-3-12z" fill="#f2bfcc"/></svg>
  <div><div class="lbl">Call us Today</div><div class="num">555.014.2290</div></div>
</div>

<nav class="abs nav">
  <a class="active" style="width:132px">Home</a>
  <a style="width:195px">Who Is Ray Dunmore</a>
  <a style="width:306px">Why Ray Is Sharing His Secrets</a>
  <a style="width:148px;border-right:0">Contact</a>
</nav>

<div class="abs video">
  <div class="shot" role="img" aria-label="Video still of a bakery showroom display"></div>
  <div class="title">Showroom Display Walkthrough</div>
  <div class="play"><svg width="68" height="46"><path d="M28 15l16 8-16 8z" fill="#fff"/></svg></div>
  <div class="track"></div>
  <div class="bar"><svg width="30" height="28" style="position:absolute;left:16px"><path d="M6 9l10 5-10 5z" fill="#ccc"/></svg></div>
  <div class="time">0:00 / 4:51</div>
  <div class="brand">Player</div>
</div>

<aside class="abs optin">
  <div class="top"><b>FREE</b> Videos To Help<br>You Sell More Wedding<br>Cakes At Higher<br>Prices... Immediately</div>
  <div class="field" style="top:160px"><svg width="14" height="13"><circle cx="7" cy="4" r="3.5" fill="#aaa"/><path d="M0 13c0-5 14-5 14 0z" fill="#aaa"/></svg>Name</div>
  <div class="field" style="top:198px"><svg width="14" height="10"><rect width="14" height="10" fill="#aaa"/><path d="M0 0l7 6 7-6" stroke="#fff" fill="none"/></svg>Email</div>
  <div class="nospam">No Spam. I Promise.</div>
  <div class="btn">Get Instant Access</div>
</aside>

<div class="abs rule" style="top:530px"></div>
<h2 class="abs section-title">3 Leading-Edge Techniques for Convincing Brides to Choose You</h2>

<div class="card" style="left:130px">
  <div class="img" role="img" aria-label="Photo of a woman with two-tone face paint" style="background:linear-gradient(90deg,#e0a640,#3f7f7a 50%,#e9b25a)"></div>
  <h3>In the first video, discover a sales growth secret that reveals the "Two Faces Of Your Wedding Cake Business."</h3>
  <p>One side of your face displays your "Internal Reality." It's how you run your business. Whether...</p>
  <div class="btn">READ MORE</div>
</div>
<div class="card" style="left:329px">
  <div class="img" role="img" aria-label="Photo of a woman in red shrugging" style="background:linear-gradient(#e9e9e9,#dcdcdc);"><div style="position:absolute;left:60px;top:30px;width:40px;height:72px;background:#c8262c"></div></div>
  <h3>In the second video you'll peek at my most effective psychological sales secret called "The Insecurity Gap."</h3>
  <p>The #1 Reason You're Not Selling More Wedding Cakes...is due to "The Insecurity Gap" a bride...</p>
  <div class="btn">READ MORE</div>
</div>
<div class="card" style="left:528px">
  <div class="img" role="img" aria-label="Photo of a white coffee mug" style="background:linear-gradient(#f4f4f4,#e2e2e2)"></div>
  <h3>In the third video, you will find out how to use Your "External Perception to WIN more wedding cake orders.</h3>
  <p>Start thinking in terms of being the "World's Greatest"... not Chicago's best...</p>
  <div class="btn">READ MORE</div>
</div>
<div class="card" style="left:728px">
  <div class="img" style="background:linear-gradient(#1f4f9a,#0f2d60);display:flex;align-items:center;justify-content:center"><span style="width:90px;height:46px;background:#5b7cb8;border-radius:4px;display:block"></span></div>
  <div class="seen">Ray Dunmore as seen:</div>
  <div class="badge" style="top:152px"><span></span></div>
  <div class="badge" style="top:222px"><span></span></div>
  <div class="btn">READ MORE</div>
</div>

<div class="abs rule" style="top:943px"></div>

<svg class="arrow" style="left:138px" width="12" height="22"><path d="M10 2L2 11l8 9" stroke="#999" stroke-width="2" fill="none"/></svg>
<div class="logo-tile" style="left:174px;width:66px"><span style="width:36px;height:36px"></span></div>
<div class="logo-tile" style="left:267px;width:137px"><span style="width:110px;height:22px"></span></div>
<div class="logo-tile" style="left:432px;width:64px"><span style="width:36px;height:36px;border-radius:50%"></span></div>
<div class="logo-tile" style="left:524px;width:65px"><span style="width:40px;height:34px"></span></div>
<div class="logo-tile" style="left:616px;width:122px"><span style="width:90px;height:34px"></span></div>
<div class="logo-tile" style="left:765px;width:105px"><span style="width:76px;height:30px"></span></div>
<svg class="arrow" style="left:892px" width="12" height="22"><path d="M2 2l8 9-8 9" stroke="#999" stroke-width="2" fill="none"/></svg>

<footer class="abs footer">
  <div class="links">HOME<i>|</i>WHO IS RAY DUNMORE<i>|</i>WHY RAY IS SHARING HIS SECRETS<i>|</i>CONTACT</div>
  <div class="contact">
    <span><svg width="10" height="14"><path d="M5 0a5 5 0 0 1 5 5c0 4-5 9-5 9S0 9 0 5a5 5 0 0 1 5-5z" fill="#fff"/><circle cx="5" cy="5" r="2" fill="#888"/></svg>Street Name, City Name&nbsp; Zip Code</span>
    <span><svg width="13" height="9"><rect width="13" height="9" fill="#fff"/><path d="M0 0l6.5 5L13 0" stroke="#888" fill="none"/></svg>info@tierhouse.example</span>
    <span><svg width="12" height="12"><path d="M2 1c1-1 3 0 3 2s-1 2-1 2c1 2 2 3 3 3 0 0 1-1 2-1s3 1 2 3c-2 2-5 1-7-1S0 3 2 1z" fill="#fff"/></svg>(555) 014 2290</span>
  </div>
  <div class="split"></div>
  <div class="news">SIGN UP FOR NEWSLETTER</div>
  <div class="news-in">Your Email Address</div>
  <div class="news-btn">Subscribe</div>
</footer>

<div class="abs bottom">Copyright © 2014 The Tier House. All Rights Reserved.
  <div class="social"><span></span><span></span><span></span><span></span></div>
</div>
</body>
</html>
```